Interior Design & consultancy firm requires a new business card design that is a little bit funky bu

Meridale Design Services is a leading strategic design practice specialising in the development and implementation of strategies and design solutions for commercial workplaces across a wide variety of industries.

The company has over twenty years experience in the strategic design, development and construction of innovative and efficient workplace environments for the commercial, corporate and industrial sectors.

We believe good design and efficient workspaces can transform companies, improve people’s lives and increase productivity.

Target Market(s)

My clients are mainly Government or corporate clients wanting to create a statement with their office fitout & new furniture that reflects their corporate identity

Industry/Entity Type

Construction

Font styles to use
Sans Serif

Colors
add136

Requirements
Must have
• The business card must be easy to read, simple & highlight my name & mobile phone number
Should not have
• I do not want the card to be fussy, feature too many colours or look to busy.

```html
<!DOCTYPE html>
<html lang="en">
<head>
<meta charset="utf-8">
<title>Meridale Design Services – Business Card</title>
<link rel="stylesheet" href="https://fonts.googleapis.com/css2?family=Open+Sans:wght@300;400;700&display=swap">
<style>
  :root {
    --brand-green: #2f7a3c;
    --ornament-green: #3d7f48;
    --ornament-soft: #cfe3d2;
    --ink: #1e1e1e;
    --card: #ffffff;
    --backdrop: #ecebe8;
    --card-shadow: rgba(0, 0, 0, 0.14);
  }
  * { margin: 0; padding: 0; box-sizing: border-box; }
  html, body {
    width: 1200px;
    height: 800px;
    overflow: hidden;
  }
  body {
    background: var(--backdrop);
    font-family: "Open Sans", sans-serif;
    display: flex;
    align-items: center;
    justify-content: center;
    gap: 50px;
  }
  .card {
    position: relative;
    width: 520px;
    height: 317px;
    background: var(--card);
    box-shadow: 0 6px 18px var(--card-shadow);
    overflow: hidden;
  }

  /* Shared brand block: flourish band, name, line, flourish band */
  .brand {
    position: absolute;
    display: flex;
    flex-direction: column;
    align-items: center;
    color: var(--brand-green);
    text-align: center;
  }
  .brand__name { font-weight: 400; line-height: 1; letter-spacing: 0.02em; }
  .brand__line { font-weight: 400; color: var(--ink); }
  .flourish {
    position: relative;
    display: flex;
    align-items: center;
    justify-content: center;
  }
  .flourish__rule {
    position: absolute;
    left: 0;
    right: 0;
    top: 50%;
    height: 1.5px;
    background: var(--ornament-green);
  }
  .flourish__fill {
    position: relative;
    height: 100%;
    border-radius: 40% / 50%;
    background: radial-gradient(ellipse at center, var(--ornament-green) 0%, var(--ornament-soft) 75%, rgba(207, 227, 210, 0) 100%);
  }

  /* Back: contact side */
  .contact {
    position: absolute;
    left: 40px;
    top: 190px;
    display: flex;
    flex-direction: column;
    gap: 2px;
  }
  .contact__name {
    font-weight: 700;
    font-size: 21px;
    color: var(--brand-green);
  }
  .contact__role {
    font-weight: 400;
    font-size: 13px;
    color: var(--ink);
  }
  .contact__mobile {
    font-weight: 700;
    font-size: 22px;
    color: var(--ink);
    letter-spacing: 0.01em;
  }
  .contact__mobile-label { color: var(--brand-green); }

  .brand--small { right: 34px; top: 28px; width: 190px; }
  .brand--small .flourish { width: 190px; height: 26px; }
  .brand--small .flourish__fill { width: 120px; }
  .brand--small .brand__name { font-size: 40px; margin-top: 8px; }
  .brand--small .brand__line { font-size: 11px; margin: 6px 0 8px; }

  /* Front: brand side */
  .brand--large { left: 0; right: 0; top: 50%; transform: translateY(-50%); }
  .brand--large .flourish { width: 440px; height: 52px; }
  .brand--large .flourish__fill { width: 280px; }
  .brand--large .brand__name { font-size: 72px; margin-top: 14px; }
  .brand--large .brand__line { font-size: 20px; margin: 8px 0 14px; }
</style>
</head>
<body>

  <section class="card card--back" aria-label="Business card, contact side">
    <div class="brand brand--small">
      <div class="flourish">
        <span class="flourish__rule"></span>
        <span class="flourish__fill" role="img" aria-label="Green ornamental scroll flourish"></span>
      </div>
      <p class="brand__name">Meridale</p>
      <p class="brand__line">Design Services Pty Ltd</p>
      <div class="flourish">
        <span class="flourish__rule"></span>
        <span class="flourish__fill" role="img" aria-label="Green ornamental scroll flourish"></span>
      </div>
    </div>
    <div class="contact">
      <p class="contact__name">Karen Whitfield</p>
      <p class="contact__role">Director &amp; senior interior designer</p>
      <p class="contact__mobile"><span class="contact__mobile-label">Mobile</span> 0400 555 218</p>
    </div>
  </section>

  <section class="card card--front" aria-label="Business card, brand side">
    <div class="brand brand--large">
      <div class="flourish">
        <span class="flourish__rule"></span>
        <span class="flourish__fill" role="img" aria-label="Green ornamental scroll flourish"></span>
      </div>
      <p class="brand__name">Meridale</p>
      <p class="brand__line">Design Services Pty Ltd</p>
      <div class="flourish">
        <span class="flourish__rule"></span>
        <span class="flourish__fill" role="img" aria-label="Green ornamental scroll flourish"></span>
      </div>
    </div>
  </section>

</body>
</html>
```